Eye catching Bottle label for pink gin targeting women 25+

We need a new label for a re-launch of our shimmering strawberry pink gin liqueur. We would like it to look premium and eye catching on the shelf. We have 2 labels we require, one for 200ml bottle (2x2 inches) and one for 500ml bottle 4x4 inches). Label must state the ml of the bottle abd that it is 18.75%Vol. Also say Shimmering Strawberry Gin Liqueur with the brand name at the top - Harlow Vale Distillers. We have a logo but it doesn't need to be used if it doesn't work with the design/colours. The gin is presented in a clear bottle and is pink and sparkly. See uploaded image for reference.

Target Market(s)

Women aged 25-45

Font styles to use
Decorative

Colors
f59296
fbd4d5
eea4c8

Requirements
Must have
• Bottle size - 500ml/200ml
• Must say 18.75% Vol
• Must have brand name - Harlow Vale Distillers
• Must have product name - Glistening Rose Berry
• Must say - Gin Liqueur
Nice to have
• Some sort of floral or swirley background detail would be nice
Should not have
• Must not appeal to children

```html
<!DOCTYPE html>
<html lang="en">
<head>
<meta charset="utf-8">
<title>Harlow Vale Distillers – Glistening Rose Berry Gin Liqueur Label</title>
<link rel="stylesheet" href="https://fonts.googleapis.com/css2?family=Playfair+Display:wght@700&family=Montserrat:wght@400;500;700&display=swap">
<style>
  :root {
    --page-bg: #f4f1f3;
    --label-pink: #f8cfdc;
    --ink: #1c1418;
    --ink-soft: #4a3a42;
    --art-violet: #c978c9;
    --art-rose: #f59296;
    --art-dark: #2a1a24;
  }

  * { margin: 0; padding: 0; box-sizing: border-box; }

  html, body {
    width: 1200px;
    height: 808px;
    overflow: hidden;
    background: var(--page-bg);
  }

  .canvas {
    position: relative;
    width: 1200px;
    height: 808px;
  }

  .label {
    position: absolute;
    left: 240px;
    top: 44px;
    width: 720px;
    height: 720px;
    background: var(--label-pink);
    overflow: hidden;
  }

  .label__artwork {
    position: absolute;
    left: 300px;
    top: 120px;
    width: 380px;
    height: 500px;
  }

  .label__brand {
    position: absolute;
    left: 124px;
    top: 108px;
    font-family: "Montserrat", sans-serif;
    font-weight: 700;
    font-size: 22px;
    letter-spacing: 3px;
    color: var(--ink);
    text-transform: uppercase;
  }

  .label__product {
    position: absolute;
    left: 122px;
    top: 196px;
    font-family: "Playfair Display", serif;
    font-weight: 700;
    font-size: 60px;
    line-height: 90px;
    letter-spacing: 1px;
    color: var(--ink);
    text-transform: uppercase;
  }

  .label__product span { display: block; }

  .label__type {
    position: absolute;
    left: 124px;
    top: 506px;
    font-family: "Montserrat", sans-serif;
    font-weight: 500;
    font-size: 27px;
    letter-spacing: 2.5px;
    color: var(--ink);
    text-transform: uppercase;
  }

  .label__details {
    position: absolute;
    left: 124px;
    top: 580px;
    font-family: "Montserrat", sans-serif;
    font-size: 20px;
    letter-spacing: 1px;
    color: var(--ink-soft);
  }

  .label__abv {
    margin-left: 20px;
    color: var(--ink);
  }

  .label__abv strong { font-weight: 500; }
</style>
</head>
<body>
  <main class="canvas">
    <section class="label">
      <svg class="label__artwork" viewBox="0 0 380 500" role="img" aria-label="Illustration of sketched strawberries wrapped in a swirling black and violet ornamental flourish">
        <defs>
          <linearGradient id="artwork-tones" x1="0" y1="0" x2="0.6" y2="1">
            <stop offset="0" stop-color="#c978c9" stop-opacity="0.55"/>
            <stop offset="0.45" stop-color="#f59296" stop-opacity="0.55"/>
            <stop offset="1" stop-color="#2a1a24" stop-opacity="0.45"/>
          </linearGradient>
        </defs>
        <path d="M150 10 C260 -5 370 50 360 150 C352 230 300 270 320 350 C338 430 280 495 210 490 C150 486 120 440 130 380 C140 320 110 290 100 220 C90 130 70 25 150 10 Z" fill="url(#artwork-tones)"/>
      </svg>

      <p class="label__brand">Harlow Vale Distillers</p>

      <h1 class="label__product">
        <span>Glistening</span>
        <span>Rose</span>
        <span>Berry</span>
      </h1>

      <p class="label__type">Gin Liqueur</p>

      <p class="label__details">500ml<span class="label__abv"><strong>18.75%</strong> Vol</span></p>
    </section>
  </main>
</body>
</html>
```